Development of musical artist Torvan Quell's Website

I need a website designed for a reggae musical artist by the name of Torvan Quell. The site should be representative of a Reggae artist from Jamaica that has a Caribbean appeal but also attractive to global audiences. The website should be responsive for all devices (desktop, laptop, mobile). It should be optimized for SEO purposes. Icons for Instagram, Facebook, Twitter, YouTube should be included. The sections of the website should be as follows: Home, Media, News, Bio, Join, Contact. The 'Join' section should be a form for database collection to the fan club. I would like to easily be able to dump this database in an excel or .csv file at any given time. The 'Media' section should be able to showcase video thumbnails and allow persons to play videos through the site and the videos will be fed from YouTube. The 'News' section will be for announcements and or new releases where the artist is mentioned. The site should also be built in such a way that analytics can be easily implemented. This website should be the main call to action for this artist moving forward. I would also like the website to have a easy to use CMS platform (Wordpress perhaps). The URL for the website will be torvanquellstar.example. Here are the links for some of the social media pages:
YouTube - https://www.videohub.example/user/TorvanQuell
Instagram - https://www.snapgram.example/torvanquell/
A good website to refer to from a design perspective is https://maldoreef.example/

Target Market(s)

Reggae and Pop music fans

Industry/Entity Type

Artists

Coding

Coded - Design and coding required

Number of Pages Required

5+ page

Font styles to use
Sans Serif

Requirements
Must have
• Great design
Nice to have
• Parallax technology

```html
<!DOCTYPE html>
<html lang="en">
<head>
<meta charset="utf-8">
<title>Torvan Quell — Website Design</title>
<link href="https://fonts.googleapis.com/css2?family=Poppins:wght@400;500;600;700&display=swap" rel="stylesheet">
<style>
:root{
  --backdrop:#1f1f1f;
  --ink:#111;
  --muted:#8a8a8a;
  --rule:#e6e6e6;
  --paper:#fff;
  --soft:#f3f3f3;
  --sun:#fbeb95;
  --sand:#d7b98b;
  --accent:#d8242a;
  --night:#0b0b0b;
}
*{box-sizing:border-box;margin:0;padding:0}
html,body{width:1200px;height:1200px;overflow:hidden;background:var(--backdrop);font-family:"Poppins",sans-serif;color:var(--ink)}
.abs{position:absolute}
.board{position:relative;width:1200px;height:1200px}

/* ---------- full page overview ---------- */
.overview{position:absolute;left:0;top:0;width:317px;height:1200px;background:var(--paper);overflow:hidden}
.hero{position:absolute;left:0;top:0;width:317px;height:140px;background:linear-gradient(90deg,#050505 0%,#120806 45%,#4a2415 62%,#2a140c 78%,#080404 100%);color:#fff}
.brand{left:12px;top:7px;font-size:5px;font-weight:700;letter-spacing:.3px;color:#fff;display:flex;align-items:center;gap:3px}
.brand i{width:4px;height:4px;background:var(--accent);display:inline-block}
.nav{right:10px;top:5px;display:flex;gap:6px;font-size:3px;color:#ddd}
.hero h1{left:36px;top:34px;font-size:22px;line-height:20px;font-weight:700;letter-spacing:-1px}
.hero .sub{left:37px;top:84px;font-size:3.5px;color:#ccc}
.badge{top:99px;width:27px;height:9px;border:.5px solid #888;border-radius:1.5px;background:#111}
.arrow{top:70px;font-size:9px;color:#fff}
.countdown{position:absolute;left:0;top:140px;width:317px;height:94px;background:var(--sun);text-align:center}
.countdown .tiny{font-size:2.6px;color:#555;margin-top:17px}
.countdown h3{font-size:8px;font-weight:500;margin-top:3px}
.count-row{display:flex;justify-content:center;gap:25px;margin-top:5px}
.count-row b{display:block;font-size:16px;font-weight:500;width:28px}
.count-row span{font-size:3px;color:#555}
.mini-media{position:absolute;left:0;top:234px;width:317px;height:166px;background:var(--paper)}
.label-xs{font-size:3px;color:var(--muted)}
.cover{position:absolute;width:66px;height:66px;box-shadow:0 3px 4px rgba(0,0,0,.15)}
.cover-a{background:linear-gradient(135deg,#d8b46b,#8a5a2e 55%,#c89a55)}
.cover-b{background:linear-gradient(180deg,#7fb2c9,#b99a6e 55%,#3d2a1c)}
.cover-c{background:linear-gradient(135deg,#6a6a6a,#3b2620 55%,#8a8a8a)}
.mini-videos{position:absolute;left:0;top:400px;width:317px;height:66px;display:flex}
.vid-a{background:radial-gradient(circle at 50% 60%,#7a0d10,#2a0405 80%)}
.vid-b{background:radial-gradient(circle at 45% 50%,#ff3a1c,#8d0e08 40%,#1a0302 85%)}
.mini-tour{position:absolute;left:0;top:466px;width:317px;height:196px;background:var(--paper)}
.mt-row{position:absolute;left:50px;width:219px;height:17px;border-bottom:.5px solid var(--rule);display:flex;align-items:center;font-size:3.2px}
.mt-row b{font-size:9px;font-weight:600;width:16px}
.mt-row .md{width:14px;font-size:2.6px;line-height:3px;color:#555}
.mt-row .ev{flex:1;font-weight:600}
.mt-row .st{font-size:2.4px}
.mini-gallery{position:absolute;left:0;top:662px;width:317px;height:160px}
.mini-blog{position:absolute;left:0;top:822px;width:317px;height:170px;background:var(--soft)}
.post{position:absolute;top:49px;width:71px;height:85px;background:#fff;box-shadow:0 1px 3px rgba(0,0,0,.1)}
.post .ph{height:43px}
.post h5{font-size:3.2px;font-weight:600;margin:5px 5px 1px}
.post p{font-size:2.4px;color:#999;margin:0 5px;line-height:3.6px}
.mini-news{position:absolute;left:0;top:992px;width:317px;height:82px;background:var(--sand);color:#fff}
.mini-contact{position:absolute;left:0;top:1074px;width:317px;height:66px;background:var(--soft);font-size:3px}
.mini-contact .col{position:absolute;top:21px}
.mini-contact h6{font-size:4.5px;font-weight:500;margin-bottom:4px}
.mini-contact b{display:block;font-size:3px;font-weight:600}
.mini-contact span{display:block;font-size:2.2px;color:#888;line-height:3.4px}
.mini-footer{position:absolute;left:0;top:1140px;width:317px;height:60px;background:var(--night);color:#fff;text-align:center}
.mini-footer h4{font-size:6.5px;font-weight:700;margin-top:21px}
.mini-footer p{font-size:2.4px;color:#aaa;line-height:4px}
.dots{display:flex;justify-content:center;gap:4px;margin-top:2px}
.dots i{width:3px;height:3px;border-radius:50%;background:#aaa}

/* ---------- section close-up ---------- */
.closeup{position:absolute;left:359px;top:0;width:782px;height:1200px;background:var(--paper);overflow:hidden}
.media-label{left:125px;top:45px;font-size:7px;color:var(--muted)}
.media-title{left:125px;top:60px;font-size:18px;font-weight:500}
.title-dash{left:125px;top:93px;width:14px;height:2px;background:var(--ink)}
.album{position:absolute;top:120px;width:161px;height:161px;box-shadow:0 6px 8px rgba(0,0,0,.15)}
.deco{position:absolute;background:#e4e4e4}
.player{position:absolute;left:125px;top:297px;width:660px;height:28px}
.player .thumb{position:absolute;left:0;top:0;width:28px;height:28px;background:linear-gradient(135deg,#4a2a1a,#120a06)}
.player .track{position:absolute;left:42px;top:3px;font-size:8.5px;font-weight:500}
.player .artist{position:absolute;left:42px;top:15px;font-size:6px;color:#aaa}
.ctrl{position:absolute;top:8px}
.bar{position:absolute;height:1px;background:#ccc;top:14px}
.section-head{position:absolute;left:0;width:782px;text-align:center;font-weight:500;text-transform:uppercase}
.videos{position:absolute;left:0;top:408px;width:782px;height:164px;display:flex}
.videos .tile{position:relative}
.play{position:absolute;left:50%;top:50%;transform:translate(-50%,-50%)}
.tour-row{position:absolute;left:125px;width:538px;height:42.4px;border-bottom:1px solid var(--rule);display:flex;align-items:center}
.tour-row .day{width:37px;font-size:24px;font-weight:500;letter-spacing:-.5px}
.tour-row .md{width:32px;font-size:8.5px;line-height:11px;color:#444;text-align:center}
.tour-row .ev{flex:1;font-size:9.5px;font-weight:500}
.tour-row .st{font-size:6px;font-weight:500}
.view-all{position:absolute;left:359px;top:925px;width:72px;height:21px;background:var(--night);color:#fff;font-size:6px;font-weight:600;display:flex;align-items:center;justify-content:center}
.gallery{position:absolute;left:0;top:1058px;width:782px;height:142px;display:flex}
</style>
</head>
<body>
<div class="board">

  <!-- Full page overview -->
  <section class="overview" aria-label="Home page overview">
    <header class="hero">
      <div class="abs" role="img" aria-label="Portrait photo of the artist in warm light" style="left:150px;top:0;width:130px;height:140px;background:radial-gradient(ellipse at 50% 45%,rgba(120,60,30,.55),rgba(0,0,0,0) 70%)"></div>
      <div class="abs brand"><i></i>TORVAN QUELL</div>
      <nav class="abs nav"><span>Home</span><span>Media</span><span>News</span><span>Bio</span><span>Join</span><span>Contact</span></nav>
      <h1 class="abs">New Album<br>Out Now</h1>
      <p class="abs sub">Available on all platforms, stream or purchase today</p>
      <span class="abs badge" style="left:38px"></span>
      <span class="abs badge" style="left:70px;width:25px"></span>
      <span class="abs arrow" style="left:5px">‹</span>
      <span class="abs arrow" style="right:5px">›</span>
    </header>

    <section class="countdown">
      <p class="tiny">Kingston Jamaica – Club Harbour</p>
      <h3>Next Performance</h3>
      <div class="count-row">
        <div><b>54</b><span>Days</span></div>
        <div><b>21</b><span>Hours</span></div>
        <div><b>48</b><span>Minutes</span></div>
        <div><b>52</b><span>Seconds</span></div>
      </div>
    </section>

    <section class="mini-media">
      <span class="abs" style="left:21px;top:13px;width:8px;height:8px;border:1px solid #ccc;border-radius:50%"></span>
      <span class="abs" style="left:35px;top:119px;width:9px;height:9px;border:1.2px solid #ccc;border-radius:50%"></span>
      <span class="abs" style="left:20px;top:162px;width:6px;height:6px;background:#ddd;border-radius:50%"></span>
      <p class="abs label-xs" style="left:50px;top:19px">Media</p>
      <h3 class="abs" style="left:50px;top:25px;font-size:6.5px;font-weight:500">Latest Albums / Singles</h3>
      <span class="abs" style="left:50px;top:36px;width:5px;height:1px;background:#111"></span>
      <div class="cover cover-a" style="left:50px;top:49px" role="img" aria-label="Album cover artwork"></div>
      <div class="cover cover-b" style="left:127px;top:49px" role="img" aria-label="Single cover artwork"></div>
      <div class="cover cover-c" style="left:203px;top:49px" role="img" aria-label="Single cover artwork"></div>
      <span class="abs" style="left:50px;top:122px;width:11px;height:11px;background:#3a2014"></span>
      <span class="abs" style="left:66px;top:123px;font-size:3.5px;font-weight:600">Hype</span>
      <span class="abs" style="left:66px;top:128px;font-size:2.4px;color:#aaa">Torvan Quell</span>
      <span class="abs" style="left:108px;top:125px;font-size:3px">⏮ &nbsp;&nbsp;&nbsp; ▶ &nbsp;&nbsp;&nbsp; ⏭</span>
      <span class="abs" style="left:210px;top:127px;width:17px;height:.5px;background:#bbb"></span>
      <span class="abs" style="left:247px;top:127px;width:17px;height:.5px;background:#333"></span>
      <p class="abs" style="left:0;width:317px;text-align:center;top:145px;font-size:5.5px;font-weight:500">LATEST VIDEOS</p>
    </section>

    <section class="mini-videos">
      <div class="vid-a" style="width:160px;position:relative" role="img" aria-label="Concert crowd in red light">
        <svg class="play" width="12" height="12" viewBox="0 0 24 24"><circle cx="12" cy="12" r="10.5" fill="none" stroke="#fff" stroke-width="2"/><path d="M10 7.5l6 4.5-6 4.5z" fill="#fff"/></svg>
      </div>
      <div class="vid-b" style="width:157px;position:relative" role="img" aria-label="Close-up in neon red light">
        <svg class="play" width="12" height="12" viewBox="0 0 24 24"><circle cx="12" cy="12" r="10.5" fill="none" stroke="#fff" stroke-width="2"/><path d="M10 7.5l6 4.5-6 4.5z" fill="#fff"/></svg>
      </div>
    </section>

    <section class="mini-tour">
      <p class="abs" style="left:0;width:317px;text-align:center;top:18px;font-size:4.5px;font-weight:500">TOUR DATES</p>
      <div class="mt-row" style="top:24px"><b>10</b><span class="md">Jun<br>Sun</span><span class="ev">Chelmsford, UK – Vale Fest</span><span class="st">sold out!</span></div>
      <div class="mt-row" style="top:41px"><b>13</b><span class="md">Jun<br>Wed</span><span class="ev">Sheffield, UK – Tramway Sounds</span><span class="st">» buy tickets</span></div>
      <div class="mt-row" style="top:58px"><b>15</b><span class="md">Jun<br>Fri</span><span class="ev">Kostrzyn, Poland – Oakridge Fest</span><span class="st">» buy tickets</span></div>
      <div class="mt-row" style="top:75px"><b>17</b><span class="md">Jun<br>Sun</span><span class="ev">Lisbon, Portugal – Rock on the Tagus</span><span class="st">free!</span></div>
      <div class="mt-row" style="top:92px"><b>20</b><span class="md">Jun<br>Wed</span><span class="ev">Pilton, UK – Meadowbank</span><span class="st">» buy tickets</span></div>
      <div class="mt-row" style="top:109px"><b>22</b><span class="md">Jun<br>Fri</span><span class="ev">Bremen, Germany – Gale Fest</span><span class="st">sold out!</span></div>
      <span class="abs" style="left:145px;top:144px;width:29px;height:8px;background:#111;color:#fff;font-size:2.4px;display:flex;align-items:center;justify-content:center">view all</span>
      <p class="abs" style="left:0;width:317px;text-align:center;top:184px;font-size:5.5px;font-weight:600">GALLERY</p>
    </section>

    <section class="mini-gallery">
      <div class="abs" role="img" aria-label="Street scene with painted wall and car" style="left:0;top:0;width:160px;height:82px;background:linear-gradient(180deg,#6f9a4e,#c24d4a 50%,#9aa0a6)"></div>
      <div class="abs" role="img" aria-label="Dancer with raised arms" style="left:160px;top:0;width:81px;height:82px;background:linear-gradient(135deg,#f3b9a0,#c2573c)"></div>
      <div class="abs" role="img" aria-label="Portrait with teal headwrap" style="left:241px;top:0;width:76px;height:82px;background:linear-gradient(135deg,#b3463a,#2a1410 60%,#6aa0a0)"></div>
      <div class="abs" role="img" aria-label="Portrait in dark tones" style="left:0;top:82px;width:78px;height:78px;background:linear-gradient(135deg,#3a2418,#c08040)"></div>
      <div class="abs" role="img" aria-label="Illustrated artist portrait" style="left:78px;top:82px;width:82px;height:78px;background:linear-gradient(180deg,#efe7da,#d9a441 60%,#a33)"></div>
      <div class="abs" role="img" aria-label="Studio with guitars and keyboard" style="left:160px;top:82px;width:157px;height:78px;background:linear-gradient(90deg,#2e2a26,#6b5a48 60%,#a88a68)"></div>
    </section>

    <section class="mini-blog">
      <p class="abs label-xs" style="left:50px;top:20px">News</p>
      <h3 class="abs" style="left:50px;top:26px;font-size:6.5px;font-weight:500">Latest Blog Posts</h3>
      <span class="abs" style="left:50px;top:37px;width:5px;height:1px;background:#111"></span>
      <article class="post" style="left:50px"><div class="ph" role="img" aria-label="Drummer on stage" style="background:linear-gradient(135deg,#1a2a3a,#4a6a8a)"></div><h5>Jamaican Jam Sessions</h5><p>Short notes from the studio week, new riddims and guests on the way home.</p></article>
      <article class="post" style="left:125px"><div class="ph" role="img" aria-label="Musician at the mixing desk" style="background:linear-gradient(180deg,#9ac0e0,#3a3028)"></div><h5>Island Values</h5><p>Roots, family and the sound of the island carried to every new stage.</p></article>
      <article class="post" style="left:199px"><div class="ph" role="img" aria-label="Performer in red smoke" style="background:radial-gradient(circle,#e8302a,#8a0e0a)"></div><h5>Universal Vibes</h5><p>One message for every crowd, from the yard to the festival field.</p></article>
      <span class="abs" style="left:50px;top:146px;width:33px;height:8px;border:.5px solid #333;font-size:2.2px;display:flex;align-items:center;justify-content:center">view more</span>
    </section>

    <section class="mini-news">
      <h3 class="abs" style="left:50px;top:22px;font-size:6.2px;font-weight:500">Subscribe To The Newsletter</h3>
      <span class="abs" style="left:50px;top:35px;font-size:2.4px;opacity:.8">Your email</span>
      <span class="abs" style="left:50px;top:41px;width:108px;height:.5px;background:#fff"></span>
      <span class="abs" style="left:50px;top:54px;width:26px;height:8px;background:#fff;color:#333;font-size:2.4px;display:flex;align-items:center;justify-content:center">subscribe</span>
    </section>

    <section class="mini-contact">
      <div class="col" style="left:50px"><h6>Press</h6><b>Jon Doe</b><span>press@torvanquellstar.example</span><span>+1 876 555 0101</span></div>
      <div class="col" style="left:106px"><h6>Management</h6><b>Jane Doe</b><span>mgmt@torvanquellstar.example</span><span>+1 876 555 0102</span></div>
      <div class="col" style="left:162px"><h6>Booking</h6><b>Ben Doe</b><span>book@torvanquellstar.example</span><span>+1 876 555 0103</span></div>
      <div class="col" style="left:218px"><h6>Label</h6><b>Monica Doe</b><span>label@torvanquellstar.example</span><span>+1 876 555 0104</span></div>
    </section>

    <footer class="mini-footer">
      <h4>TORVANQUELL.</h4>
      <p>Copyright @torvanquellstar.example</p>
      <p>+1 876 555 0100 · info@torvanquellstar.example</p>
      <div class="dots"><i></i><i></i><i></i><i></i><i></i></div>
    </footer>
  </section>

  <!-- Section close-up -->
  <section class="closeup" aria-label="Media and tour section">
    <svg class="abs" style="left:50px;top:18px" width="40" height="30" viewBox="0 0 40 30"><circle cx="14" cy="18" r="8" fill="none" stroke="#c8c8c8" stroke-width="1.5"/><path d="M14 18l5-4" stroke="#c8c8c8" stroke-width="1.5"/></svg>
    <span class="deco" style="left:67px;top:62px;width:9px;height:9px;border-radius:50%"></span>
    <span class="deco" style="left:150px;top:24px;width:18px;height:14px"></span>
    <span class="deco" style="left:14px;top:128px;width:16px;height:16px;transform:rotate(45deg)"></span>
    <span class="deco" style="left:103px;top:90px;width:14px;height:14px;transform:rotate(45deg)"></span>
    <svg class="abs" style="left:85px;top:124px" width="36" height="36" viewBox="0 0 36 36"><circle cx="18" cy="18" r="15.5" fill="none" stroke="#c8c8c8" stroke-width="2.5"/></svg>
    <span class="deco" style="left:52px;top:266px;width:20px;height:20px;border-radius:50%"></span>
    <span class="deco" style="left:86px;top:318px;width:14px;height:14px;transform:rotate(45deg)"></span>
    <span class="deco" style="left:648px;top:380px;width:16px;height:16px;border-radius:50%"></span>
    <span class="abs" style="left:719px;top:378px;width:28px;height:28px;border:2px solid #c8c8c8;border-radius:50%"></span>
    <span class="abs" style="left:755px;top:332px;width:24px;height:24px;border:2px solid #c8c8c8;transform:rotate(45deg)"></span>

    <p class="abs media-label">Media</p>
    <h2 class="abs media-title">Latest Albums / Singles</h2>
    <span class="abs title-dash"></span>

    <div class="album cover-a" style="left:125px" role="img" aria-label="Album cover artwork in warm painted tones"></div>
    <div class="album cover-b" style="left:314px" role="img" aria-label="Single cover: figure on a beach"></div>
    <div class="album cover-c" style="left:502px" role="img" aria-label="Single cover: painted profile portrait"></div>

    <div class="player">
      <div class="thumb" role="img" aria-label="Track artwork"></div>
      <span class="track">Hype</span>
      <span class="artist">Torvan Quell</span>
      <svg class="ctrl" style="left:138px" width="9" height="9" viewBox="0 0 10 10"><rect x="1" y="1.5" width="1.4" height="7" fill="#222"/><path d="M9 1.5v7L3 5z" fill="#222"/></svg>
      <svg class="ctrl" style="left:178px" width="8" height="9" viewBox="0 0 8 10"><path d="M1 1v8l6-4z" fill="#222"/></svg>
      <svg class="ctrl" style="left:218px" width="9" height="9" viewBox="0 0 10 10"><path d="M1 1.5v7L7 5z" fill="#222"/><rect x="7.6" y="1.5" width="1.4" height="7" fill="#222"/></svg>
      <span class="bar" style="left:262px;width:123px"></span>
      <span class="abs" style="left:396px;top:10px;font-size:6.5px;color:#aaa">00:00/00:30</span>
      <svg class="ctrl" style="left:469px;top:10px" width="7" height="7" viewBox="0 0 10 10"><path d="M1 3.5h2.5L7 1v8L3.5 6.5H1z" fill="#333"/></svg>
      <span class="bar" style="left:485px;width:43px;background:#222"></span>
    </div>

    <h2 class="section-head" style="top:355px;font-size:16px">Latest Videos</h2>

    <section class="videos">
      <div class="tile vid-a" style="width:395px" role="img" aria-label="Concert crowd with raised hands in red light">
        <svg class="play" width="32" height="32" viewBox="0 0 24 24"><circle cx="12" cy="12" r="10.5" fill="none" stroke="#fff" stroke-width="1.8"/><path d="M10 7.5l6 4.5-6 4.5z" fill="#fff"/></svg>
      </div>
      <div class="tile vid-b" style="width:387px" role="img" aria-label="Close-up with glowing sunglasses in red neon">
        <svg class="play" width="32" height="32" viewBox="0 0 24 24"><circle cx="12" cy="12" r="10.5" fill="none" stroke="#fff" stroke-width="1.8"/><path d="M10 7.5l6 4.5-6 4.5z" fill="#fff"/></svg>
      </div>
    </section>

    <h2 class="section-head" style="top:613px;font-size:13px">Tour Dates</h2>
    <div class="tour-row" style="top:629px"><span class="day">10</span><span class="md">Jun<br>Sun</span><span class="ev">Chelmsford, UK – Vale Fest</span><span class="st">sold out!</span></div>
    <div class="tour-row" style="top:671px"><span class="day">13</span><span class="md">Jun<br>Wed</span><span class="ev">Sheffield, UK – Tramway Sounds</span><span class="st">» buy tickets</span></div>
    <div class="tour-row" style="top:714px"><span class="day">15</span><span class="md">Jun<br>Fri</span><span class="ev">Kostrzyn, Poland – Oakridge Fest</span><span class="st">» buy tickets</span></div>
    <div class="tour-row" style="top:756px"><span class="day">17</span><span class="md">Jun<br>Sun</span><span class="ev">Lisbon, Portugal – Rock on the Tagus</span><span class="st">free!</span></div>
    <div class="tour-row" style="top:798px"><span class="day">20</span><span class="md">Jun<br>Wed</span><span class="ev">Pilton, UK – Meadowbank</span><span class="st">» buy tickets</span></div>
    <div class="tour-row" style="top:841px"><span class="day">22</span><span class="md">Jun<br>Fri</span><span class="ev">Bremen, Germany – Gale Fest</span><span class="st">sold out!</span></div>
    <span class="view-all">view all</span>

    <h2 class="section-head" style="top:1026px;font-size:16px;font-weight:600">Gallery</h2>
    <section class="gallery">
      <div style="width:395px;background:linear-gradient(180deg,#7fa65a 0%,#5a8040 35%,#c8484a 55%,#b8bcc2 80%,#8a8e94 100%)" role="img" aria-label="Street scene with a painted wall and parked car"></div>
      <div style="width:200px;background:linear-gradient(135deg,#f6c4ae,#e2866c 50%,#b84a34)" role="img" aria-label="Dancer with raised arms against a warm sky"></div>
      <div style="width:187px;background:linear-gradient(135deg,#c04a3e,#3a1c16 55%,#5a9a9a)" role="img" aria-label="Portrait with teal headwrap"></div>
    </section>
  </section>

</div>
</body>
</html>
```